Landing page for buying gold and stamps

Create a landing page for our purchase. We buy postage stamps, franked goods, gold coins, scrap gold, silver money, etc. We don't want to sell anything to people, we just shop. So the visitors should send their old gold, their stamps, etc. by post. We then estimate the value and transfer the money by bank or you can collect it in cash.

The visitor should see what he can sell. If he fills in his contact details, he will receive our purchase form and the mailing label by post so that he can send in his sales goods free of charge. Or he can call us or write an e-mail and come to us directly.

We buy:
When the form is filled out, an email will be sent to our address with the following data:
Surname
First name
Street, Nr.
Post loan number
place
What do you want to sell

In the appendix I have added designs of flyers. You can see what we buy on it. What is missing on the flyer, however, are stamps, franking goods and rarities. In addition, the design should be similar. The logo can also be used.

In addition, the following text should be on the page:
Do you need help selling an inherited collection? Feel free to contact us. We are happy to help. We have been in the stamp and coin trade for nearly 100 years.

I have also attached a picture of the stamp as an attachment. This should also be put on the side with old gold and gold coins.

And here you will find our current purchase pages:
https://www.briefhaus-tanner.ch/ankauf-gold-und-silber
https://www.briefhaus-tanner.ch/ankauf-frankatur

Competitors' pages:
https://www.wertsachenpost.ch/goldankauf/
https://www.praegehof-lindt.ch/ankauf-1/altgold-ankauf1.html

Target Market(s)

Private persons

Font styles to use
Serif
Sans Serif

Requirements
Must have
• It must be clear that anyone who wants to sell their gold, stamps or coins can do so easily from home by post. You no longer have to go to a store.
Steps to Sell:
1. You fill out your contact details
2. We will send you a form and a label for shipping (no postage for you!)
3. You will receive a non-binding purchase offer
4. You will receive the money transferred or you can collect it in cash (or we will send you the valuables you have sent back)

You have no costs! Simply sell your gold or stamps from home.

```html
<!DOCTYPE html>
<html lang="de">
<head>
<meta charset="utf-8">
<title>Briefhaus Tanner – Ankauf Gold, Silber &amp; Briefmarken</title>
<link href="https://fonts.googleapis.com/css2?family=Cinzel:wght@700&family=Montserrat:ital,wght@0,400;0,500;0,700;1,500&display=swap" rel="stylesheet">
<style>
:root{
  --navy:#2e2680;
  --red:#e3000f;
  --footer-red:#e62a35;
  --ink:#222;
  --muted:#444;
  --line:#9a9a9a;
  --gold-1:#f3d27a;
  --gold-2:#c8962d;
  --paper:#fff;
}
*{box-sizing:border-box;margin:0;padding:0}
html,body{width:742px;height:1200px;overflow:hidden}
body{position:relative;background:var(--paper);font-family:"Montserrat",Arial,sans-serif;color:var(--ink)}
.abs{position:absolute}

.hero{left:0;top:0;width:742px;height:420px;background:linear-gradient(#e8e8e8 0%,#ececec 60%,#f7f7f7 100%)}
.rule-top{left:220px;top:55px;width:522px;height:5px;background:var(--navy);border-bottom:2px solid var(--red)}
.brand{left:107px;top:26px;display:flex;align-items:center;gap:8px}
.brand-mark{width:16px;height:16px;background:var(--red)}
.brand-name{font-weight:700;font-size:19px;color:var(--red);letter-spacing:.5px}
.cash-badge{left:568px;top:7px;width:66px;height:66px;border-radius:50%;background:radial-gradient(circle at 40% 35%,#fff 0 45%,var(--gold-1) 46% 70%,var(--gold-2) 100%);box-shadow:0 1px 4px rgba(0,0,0,.25)}

.kicker{left:107px;top:104px;width:270px;text-align:center;font-size:13px}
.headline{left:107px;top:119px;width:270px;text-align:center;font-family:"Cinzel",Georgia,serif;font-size:32px;color:var(--red);letter-spacing:.5px}
.feature{top:177px;width:85px;height:70px;border-radius:16px;background:linear-gradient(#fff,#f0f0f0);border:1px solid #ccc;box-shadow:0 2px 4px rgba(0,0,0,.12);text-align:center}
.feature-img{display:block;margin:2px auto 0;width:72px;height:38px;border-radius:40%;background:radial-gradient(ellipse,var(--gold-1),var(--gold-2) 70%,transparent 72%)}
.feature-label{display:block;margin-top:11px;font-size:8.5px;font-weight:500}
.goods{left:108px;top:265px;width:268px;height:56px;border-radius:22px;background:var(--navy);border:2px solid #fff;box-shadow:0 2px 6px rgba(0,0,0,.25);color:#fff;font-size:9.3px;line-height:14px;text-align:center;padding-top:13px}

.coins{left:410px;top:150px;width:290px;height:170px;border-radius:45%;background:radial-gradient(ellipse at 45% 45%,var(--gold-1),#d6a642 55%,var(--gold-2) 90%)}
.stamp{left:604px;top:95px;width:120px;height:120px;border-radius:50%;border:4px solid #fff;box-shadow:0 2px 6px rgba(0,0,0,.3);background:radial-gradient(circle,#e04a3c 0 40%,#d9c7b0 42% 100%)}
.rarity{left:522px;top:105px;width:72px;height:72px;border-radius:50%;background:radial-gradient(circle,#b3121c,#7d0a10);box-shadow:0 2px 5px rgba(0,0,0,.3)}
.hint{left:430px;top:336px;width:250px;text-align:center;font-size:10.5px;font-style:italic;font-weight:500;color:var(--red);line-height:14px}

.band{left:0;top:410px;width:742px;height:5px;background:var(--navy);border-bottom:2px solid var(--red)}
.call{left:259px;top:388px;width:225px;height:52px;border-radius:28px;background:#fff;border:2px solid var(--red);padding:3px}
.call span{display:flex;align-items:center;justify-content:center;height:100%;border-radius:24px;background:var(--red);color:#fff;font-weight:700;font-size:15.5px}

.help-title{left:60px;top:476px;width:622px;text-align:center;font-family:"Cinzel",Georgia,serif;font-size:22px;line-height:27px;color:var(--navy)}
.help-text{left:40px;top:540px;width:662px;text-align:center;font-size:9.4px;font-weight:500}

.form-card{left:107px;top:579px;width:528px;height:224px;border-radius:12px;background:#fff;box-shadow:0 0 8px rgba(0,0,0,.12)}
.form-head{left:111px;top:584px;width:520px;height:42px;border-radius:14px;background:var(--navy);color:#fff;font-weight:700;font-size:17px;display:flex;align-items:center;justify-content:center}
.field{width:164px;height:36px;border:1px solid var(--line);border-radius:18px;font-size:8.5px;font-weight:500;color:#333;display:flex;align-items:center;justify-content:space-between;padding:0 10px}
.caret{font-size:7px}
.submit{left:289px;top:744px;width:164px;height:36px;border-radius:18px;background:var(--red);color:#fff;font-weight:700;font-size:11px;display:flex;align-items:center;justify-content:center}

.steps-title{left:0;top:843px;width:742px;text-align:center;font-family:"Cinzel",Georgia,serif;font-size:24px;color:var(--navy)}
.step{top:898px;width:116px;height:137px;background:#fff;box-shadow:0 0 6px rgba(0,0,0,.14);text-align:center;overflow:hidden}
.step-num{position:absolute;right:0;top:0;width:34px;height:34px;border-radius:0 0 0 18px;color:#fff;font-weight:500;font-size:14px;display:flex;align-items:center;justify-content:center}
.step svg{display:block;margin:12px auto 0}
.step-title{display:block;margin-top:10px;font-family:"Cinzel",Georgia,serif;font-size:15px}
.step-text{display:block;margin-top:5px;padding:0 5px;font-size:7.7px;line-height:14px}
.red .step-num{background:var(--red)} .red .step-title{color:var(--red)}
.blue .step-num{background:var(--navy)} .blue .step-title{color:var(--navy)}

.promise{left:100px;top:1068px;width:542px;text-align:center;font-family:"Cinzel",Georgia,serif;font-size:17px;line-height:22px;color:var(--navy);text-decoration:underline;text-decoration-thickness:1px;text-underline-offset:2px}

.footer-rule{left:0;top:1146px;width:742px;height:6px;background:var(--navy)}
.footer{left:0;top:1152px;width:742px;height:48px;background:var(--footer-red);color:#fff;font-size:9px;font-weight:500;display:flex;align-items:center;justify-content:center}
</style>
</head>
<body>
<header class="abs hero">
  <div class="abs rule-top"></div>
  <div class="abs brand"><span class="brand-mark"></span><span class="brand-name">BRIEFHAUS TANNER</span></div>
  <div class="abs cash-badge" role="img" aria-label="Gold seal for instant cash payment"></div>

  <p class="abs kicker">wir suchen und kaufen</p>
  <h1 class="abs headline">GOLD &amp; SILBER</h1>

  <div class="abs feature" style="left:107px"><span class="feature-img" role="img" aria-label="Gold jewellery chains"></span><span class="feature-label">SICHER</span></div>
  <div class="abs feature" style="left:200px"><span class="feature-img" role="img" aria-label="Gold bars"></span><span class="feature-label">TRANSPARENZ</span></div>
  <div class="abs feature" style="left:293px"><span class="feature-img" role="img" aria-label="Pile of gold coins"></span><span class="feature-label">FAIR</span></div>

  <div class="abs goods">Goldvreneli&nbsp; | &nbsp;Altgold und Silber&nbsp; | &nbsp;Munzen&nbsp; | &nbsp;Barren<br>Medaillen&nbsp; | &nbsp;Uhren&nbsp; | &nbsp;Ringe&nbsp; | &nbsp;Ketten</div>

  <div class="abs coins" role="img" aria-label="Collection of gold coins"></div>
  <div class="abs rarity" role="img" aria-label="Red wax seal marking rarities"></div>
  <div class="abs stamp" role="img" aria-label="Historic postage stamp in a round frame"></div>
  <p class="abs hint">Durchsuchen Sie ihren Haushalt es Konnte sich lohnen!</p>
</header>

<div class="abs band"></div>
<a class="abs call"><span>CALL - 0041 61 555 20 40</span></a>

<section>
  <h2 class="abs help-title">Do you need help selling an inherited collection?</h2>
  <p class="abs help-text">Feel free to contact us. We are happy to help. We have been in the stamp and coin trade for nearly 100 years.</p>
</section>

<form>
  <div class="abs form-card"></div>
  <div class="abs form-head">FILL OUT THE FORM</div>
  <div class="abs field" style="left:117px;top:646px">Surname</div>
  <div class="abs field" style="left:289px;top:646px">First name</div>
  <div class="abs field" style="left:460px;top:646px">Street, Nr.</div>
  <div class="abs field" style="left:117px;top:692px">Post loan number</div>
  <div class="abs field" style="left:289px;top:692px">Place<span class="caret">▼</span></div>
  <div class="abs field" style="left:460px;top:692px">What do you want to sell<span class="caret">▼</span></div>
  <div class="abs submit">SUBMIT HERE</div>
</form>

<section>
  <h2 class="abs steps-title">Steps to Sell</h2>

  <div class="abs step red" style="left:107px">
    <span class="step-num">01</span>
    <svg width="28" height="32" viewBox="0 0 28 32" fill="none" stroke="#e3000f" stroke-width="2"><path d="M4 2h14l6 6v22H4z"/><path d="M9 12h10M9 17h10M9 22h6"/></svg>
    <span class="step-title">STEP 1</span>
    <span class="step-text">You fill out your contact details</span>
  </div>

  <div class="abs step blue" style="left:244px">
    <span class="step-num">02</span>
    <svg width="36" height="32" viewBox="0 0 36 32" fill="none" stroke="#2e2680" stroke-width="2"><circle cx="15" cy="8" r="6"/><path d="M15 5v3l2 2"/><path d="M4 16h20v10H4zM24 19h6l4 4v3H24"/><circle cx="10" cy="28" r="2.5"/><circle cx="28" cy="28" r="2.5"/></svg>
    <span class="step-title">STEP 2</span>
    <span class="step-text">We will send you a form and a label for shipping (no postage for you!)</span>
  </div>

  <div class="abs step red" style="left:382px">
    <span class="step-num">03</span>
    <svg width="32" height="32" viewBox="0 0 32 32" fill="none" stroke="#e3000f" stroke-width="2"><circle cx="16" cy="16" r="13"/><path d="M11 21l10-10"/><circle cx="11.5" cy="11.5" r="2"/><circle cx="20.5" cy="20.5" r="2"/></svg>
    <span class="step-title">STEP 3</span>
    <span class="step-text">You will receive a non-binding purchase offer</span>
  </div>

  <div class="abs step blue" style="left:519px">
    <span class="step-num">04</span>
    <svg width="34" height="32" viewBox="0 0 34 32" fill="none" stroke="#2e2680" stroke-width="2"><circle cx="17" cy="8" r="6"/><path d="M17 4v8M15 6h3a1.5 1.5 0 010 3h-2a1.5 1.5 0 000 3h3"/><path d="M2 20l6-3 9 5 9-5 6 3M8 17v10M26 17v10"/></svg>
    <span class="step-title">STEP 4</span>
    <span class="step-text">You will receive the money transferred or you can collect it in cash</span>
  </div>

  <p class="abs promise">YOU HAVE NO COSTS! SIMPLY SELL YOUR GOLD OR STAMPS FROM HOME.</p>
</section>

<div class="abs footer-rule"></div>
<footer class="abs footer">Copyrights @ 2020 Briefhaus Tanner. All Rights Reserved.</footer>
</body>
</html>
```